Letterhead & Email Signature Design

Kindly assist redesign this letterhead as well as the Email signature. I have uploaded the current designs that needs some new look

```html
<!DOCTYPE html>
<html lang="en">
<head>
<meta charset="utf-8">
<title>Ndlovu Rasebe Inc. – Email Signature</title>
<link rel="stylesheet" href="https://fonts.googleapis.com/css2?family=Montserrat:wght@400;500;600;700&display=swap">
<style>
  :root {
    --bg: #ffffff;
    --mark-grey: #8c8c8c;
    --ink-strong: #555555;
    --ink: #4a4a4a;
    --rule: #6e6e6e;
  }
  * { margin: 0; padding: 0; box-sizing: border-box; }
  html, body {
    width: 1200px;
    height: 1200px;
    overflow: hidden;
    background: var(--bg);
  }
  body {
    font-family: "Montserrat", Arial, sans-serif;
    color: var(--ink);
    display: flex;
    align-items: center;
    justify-content: center;
  }
  .signature {
    display: flex;
    align-items: flex-start;
    gap: 70px;
    width: 1000px;
  }
  .brand {
    width: 240px;
    display: flex;
    flex-direction: column;
    align-items: center;
    text-align: center;
    padding-top: 6px;
  }
  .brand-mark { display: block; margin-bottom: 24px; }
  .brand-name {
    font-size: 17px;
    font-weight: 700;
    letter-spacing: 0.5px;
    color: var(--ink-strong);
  }
  .brand-est {
    font-size: 15px;
    font-weight: 500;
    color: var(--ink-strong);
    margin-top: 4px;
  }
  .details { flex: 1; }
  .person-name {
    font-size: 22px;
    font-weight: 700;
    letter-spacing: 2.5px;
    color: var(--ink-strong);
  }
  .person-role {
    font-size: 16px;
    font-weight: 600;
    letter-spacing: 2px;
    color: var(--ink-strong);
    margin-top: 4px;
  }
  .contact { margin-top: 20px; font-size: 17px; line-height: 1.5; }
  .contact-label { font-weight: 700; font-size: 13px; letter-spacing: 0.5px; }
  .contact-web { font-weight: 700; letter-spacing: 1.5px; }
  .rule {
    height: 2px;
    background: var(--rule);
    width: 660px;
    margin: 10px 0 14px;
  }
  .address { font-size: 16px; font-weight: 500; line-height: 1.55; }
</style>
</head>
<body>
  <section class="signature">
    <div class="brand">
      <svg class="brand-mark" width="130" height="130" viewBox="0 0 130 130" aria-hidden="true">
        <circle cx="65" cy="65" r="65" fill="var(--mark-grey)"/>
      </svg>
      <p class="brand-name">NDLOVU RASEBE INC.</p>
      <p class="brand-est">Est. 2009</p>
    </div>
    <div class="details">
      <h1 class="person-name">LERATO MOKWENA</h1>
      <p class="person-role">DIRECTOR</p>
      <div class="contact">
        <p><span class="contact-label">TEL:</span> +27 12 555 0148</p>
        <p>lerato@ndlovurasebe.co.za</p>
        <p class="contact-web">www.ndlovurasebeinc.co.za</p>
      </div>
      <div class="rule"></div>
      <div class="address">
        <p>214 Marula Avenue | The Grove Office Park | Ground Floor, Building C</p>
        <p>8 Acacia Street | Fern Park | Polokwane</p>
      </div>
    </div>
  </section>
</body>
</html>
```